Limbwright Crew of Yuma Bill Board Design

We are a high class full service tree company who specializes in artistic thinning and shaping of trees in Arizona. We want to re brand our company to catch our audiences attention and hook them into calling our company on the spot. We’ve been in business for 30 years and have never truly branded our company. We want our shirts trucks and billboards to match as well as our mailing advertisement so our clientele can recognize us immediately. We are starting with our billboard first and will be following with truck and shirt designs next. Attached is a example of what we are looking for and what we’ve had designed so far. This just isn’t good enough and needs revamped if at all posssible.
- Stencil

```html
<!DOCTYPE html>
<html lang="en">
<head>
<meta charset="utf-8">
<title>Limbwright Crew of Yuma – Billboard</title>
<link href="https://fonts.googleapis.com/css2?family=Poppins:wght@800&family=Libre+Baskerville:wght@700&display=swap" rel="stylesheet">
<style>
  :root {
    --page: #eceff2;
    --white: #ffffff;
    --divider: #c9ccd0;
    --brand-blue: #2f54d3;
    --brand-brown: #48291a;
    --triangle-green: #0d9f12;
    --pill-green: #3dbd22;
    --icon-green: #17a515;
    --foliage-dark: #3f6a2c;
    --foliage-light: #8db26a;
    --sky: #7fb1e4;
    --gravel: #c9b39a;
  }
  html, body {
    margin: 0;
    padding: 0;
    width: 1200px;
    height: 1039px;
    overflow: hidden;
    background: var(--page);
  }
  .billboard {
    position: absolute;
    left: 20px;
    top: 352px;
    width: 1160px;
    height: 334px;
    overflow: hidden;
    box-shadow: 0 6px 18px rgba(0,0,0,0.18);
  }
  .billboard-art {
    position: absolute;
    inset: 0;
    width: 100%;
    height: 100%;
  }
  .headline {
    position: absolute;
    left: 0;
    width: 1160px;
    margin: 0;
    text-align: center;
    font-family: "Poppins", sans-serif;
    font-weight: 800;
    line-height: 1;
    letter-spacing: -0.5px;
  }
  .headline-top {
    top: 22px;
    font-size: 60px;
    color: var(--brand-blue);
  }
  .headline-bottom {
    top: 84px;
    font-size: 72px;
    color: var(--brand-brown);
  }
  .brand-mark {
    position: absolute;
    left: 388px;
    top: 168px;
    display: flex;
    align-items: center;
    gap: 16px;
  }
  .brand-dot {
    width: 62px;
    height: 62px;
    border-radius: 50%;
    background: var(--icon-green);
  }
  .brand-name {
    font-family: "Libre Baskerville", serif;
    font-weight: 700;
    font-size: 34px;
    line-height: 1.05;
    color: var(--brand-blue);
    text-transform: uppercase;
  }
  .phone-pill {
    position: absolute;
    left: 438px;
    top: 260px;
    width: 434px;
    height: 50px;
    border-radius: 25px;
    background: var(--pill-green);
    display: flex;
    align-items: center;
  }
  .phone-icon {
    width: 50px;
    height: 50px;
    border-radius: 50%;
    background: var(--white);
    display: flex;
    align-items: center;
    justify-content: center;
    box-sizing: border-box;
    border: 3px solid var(--pill-green);
  }
  .phone-icon-core {
    width: 40px;
    height: 40px;
    border-radius: 50%;
    background: var(--icon-green);
    display: flex;
    align-items: center;
    justify-content: center;
  }
  .phone-number {
    flex: 1;
    text-align: center;
    font-family: "Poppins", sans-serif;
    font-weight: 800;
    font-size: 44px;
    color: var(--white);
    line-height: 1;
    padding-right: 14px;
  }
</style>
</head>
<body>
  <section class="billboard">
    <svg class="billboard-art" viewBox="0 0 1617 465" preserveAspectRatio="none">
      <defs>
        <linearGradient id="canopy-photo" x1="0" y1="0" x2="0" y2="1">
          <stop offset="0" stop-color="var(--sky)"/>
          <stop offset="0.25" stop-color="var(--foliage-light)"/>
          <stop offset="1" stop-color="var(--foliage-dark)"/>
        </linearGradient>
        <linearGradient id="planting-photo" x1="0" y1="0" x2="0" y2="1">
          <stop offset="0" stop-color="var(--sky)"/>
          <stop offset="0.4" stop-color="var(--foliage-light)"/>
          <stop offset="0.6" stop-color="var(--gravel)"/>
          <stop offset="1" stop-color="#a89279"/>
        </linearGradient>
      </defs>
      <rect x="0" y="0" width="520" height="465" fill="url(#canopy-photo)" role="img" aria-label="Photo of an arborist in a bucket lift pruning a tall tree"/>
      <rect x="1100" y="0" width="517" height="465" fill="url(#planting-photo)" role="img" aria-label="Photo of a worker watering a newly planted tree in a gravel yard"/>
      <polygon class="center-panel" points="332,0 1302,0 1272,465 362,465" fill="var(--white)"/>
      <line x1="358" y1="0" x2="500" y2="465" stroke="var(--divider)" stroke-width="2"/>
      <line x1="1276" y1="0" x2="1140" y2="465" stroke="var(--divider)" stroke-width="2"/>
      <polygon class="accent-triangle" points="428,298 366,465 476,465" fill="var(--triangle-green)"/>
      <polygon class="accent-triangle" points="1218,298 1166,465 1270,465" fill="var(--triangle-green)"/>
    </svg>

    <h1 class="headline headline-top">LIMBWRIGHT CREW</h1>
    <h2 class="headline headline-bottom">OF YUMA</h2>

    <div class="brand-mark">
      <div class="brand-dot"></div>
      <div class="brand-name">Limbwright<br>Tree Care</div>
    </div>

    <div class="phone-pill">
      <div class="phone-icon">
        <div class="phone-icon-core">
          <svg width="22" height="22" viewBox="0 0 24 24" aria-hidden="true">
            <path fill="#ffffff" d="M6.6 10.8c1.4 2.8 3.8 5.1 6.6 6.6l2.2-2.2c.3-.3.7-.4 1-.2 1.1.4 2.3.6 3.6.6.6 0 1 .4 1 1V20c0 .6-.4 1-1 1C10.6 21 3 13.4 3 4c0-.6.4-1 1-1h3.5c.6 0 1 .4 1 1 0 1.3.2 2.5.6 3.6.1.3 0 .7-.2 1L6.6 10.8z"/>
          </svg>
        </div>
      </div>
      <div class="phone-number">928-555-0143</div>
    </div>
  </section>
</body>
</html>
```